Flyer Design

Hi, This work has potential to expand! After the flyers I could be looking to improve my website design and our van needs brandingPlease find attached what I would like (or if you can improve the design) on the front of my flyer. I will also provide pictures for the back. I am not sure how I want this laid out. (i have attached a picture called idea, I like this for some reason but might not work for me) My husband is young (32) and we have built a website (www.stonvale.co.uk) but we haven't gone fully live yet as he is still working for someone elseAnyway, I want to set him apart from all the rest. I want vibrant colors which is eye catchy and interesting. Makes people want to read it and not put the flyer in the binThe reason these pictures are more about conservatories, patios (smaller building work) is becasue these first lot of flyers are aimed at a new build site with 1000 homes per site. They will only be looking for conservatoies, driveways, small alterations. Maybe the conservatory could be in the middle? Again, I don't know please stick to the logo which is on the bottom left of my design but the rest is up to you. I also had a little play with the brick in the logo to maybe make it a background design somewhere. Might be rubbish ideaI did not get any help with the website so if the Flyers take the branding/colours in a different direction/theme there could be work to go forward with continuous improvement on the website AND we want to brand the vanI look forward to seeing your deignThank you for your help!Maribel
Updates
Project Deadline Extended Reason: Thank you for your efforts so far. My husband and I are reviewing the flyers and it's harder to chose the design that we like than we thought. I hope to improve the brief and interact with you more as I think we know have a better understanding of what we are looking forI will improve the brief in the next 24 hoursKind regardsSaoirse Added Saturday, January 31, 2015
Industry/Entity Type
Building
Look and feel

```html
<!DOCTYPE html>
<html lang="en">
<head>
<meta charset="utf-8">
<title>Stonvale Building Services Flyer</title>
<link href="https://fonts.googleapis.com/css2?family=Sorts+Mill+Goudy&family=Open+Sans:wght@300;400;600;700&family=Arimo:wght@400&display=swap" rel="stylesheet">
<style>
:root{
  --stage:#1e1e1e;
  --paper:#ffffff;
  --paper-shade:#f1f1f1;
  --green:#9ccb3b;
  --green-soft:#c9e392;
  --green-pale:#eaf4d6;
  --navy:#1d3a5f;
  --ink:#6a6a6a;
  --ink-dark:#4f4f4f;
  --frame:#5a5a5a;
}
*{margin:0;padding:0;box-sizing:border-box}
html,body{width:1200px;height:1200px;overflow:hidden;background:var(--stage)}
.flyer{position:absolute;background:var(--paper);overflow:hidden;box-shadow:0 2px 8px rgba(0,0,0,.5)}
.photo{position:absolute}
.brick-field{position:absolute}

/* Back */
.flyer-back{left:412px;top:38px;width:752px;height:528px}
.back-hero{left:7px;top:7px;width:246px;height:184px;background:linear-gradient(180deg,#e9ecef 0%,#b86b4b 50%,#5f8a3c 100%)}
.back-pattern{left:7px;top:198px;width:246px;height:148px;background:linear-gradient(160deg,var(--green-soft) 0%,var(--green-pale) 50%,var(--green-soft) 100%)}
.about{position:absolute;left:274px;top:26px;width:464px;font-family:"Arimo",sans-serif;font-size:12.6px;line-height:18px;color:var(--ink)}
.about p{margin-bottom:5px}
.gallery-1{left:7px;top:358px;width:246px;height:163px;background:linear-gradient(160deg,#d88bb0 0%,#f2eef2 35%,#6f9c3f 70%,#4e7a2c 100%)}
.gallery-2{left:263px;top:358px;width:238px;height:163px;background:linear-gradient(180deg,#6e8a4e 0%,#8b8478 55%,#6b6660 100%)}
.gallery-3{left:510px;top:358px;width:236px;height:163px;background:linear-gradient(180deg,#5f7d43 0%,#9a7a5c 45%,#8e6e52 100%)}

/* Front */
.flyer-front{left:36px;top:624px;width:751px;height:530px}
.front-pattern{left:0;top:0;width:751px;height:142px;clip-path:polygon(0 0,100% 0,100% 100%,55% 70%,0 30%);background:linear-gradient(180deg,var(--green-soft) 0%,var(--green-pale) 100%)}
.hero-frame{position:absolute;left:8px;top:142px;width:336px;height:238px;border:1px solid var(--frame);background:var(--paper)}
.hero-photo{left:12px;top:12px;width:310px;height:212px;background:linear-gradient(180deg,#8fae6a 0%,#eef0ee 25%,#b5563a 45%,#a04c33 70%,#5d8a3c 100%)}
.services{position:absolute;left:352px;top:145px;width:394px;font-family:"Sorts Mill Goudy",serif;color:var(--ink);text-align:center;line-height:1}
.services div{white-space:nowrap}
.footer-band{position:absolute;left:0;top:427px;width:751px;height:103px;background:linear-gradient(180deg,var(--paper-shade),var(--paper))}
.footer-rule{position:absolute;left:0;top:427px;width:356px;height:1px;background:#cfcfcf}
.brand{position:absolute;left:30px;top:437px;font-family:"Open Sans",sans-serif;color:var(--navy)}
.brand-name{display:flex;align-items:center;gap:8px;font-size:40px;font-weight:700;line-height:1}
.brand-mark{width:18px;height:18px;background:var(--green)}
.brand-tag{font-size:21px;font-weight:600;margin-top:4px;margin-left:26px}
.contact-bar{position:absolute;left:356px;top:396px;width:395px;height:31px;background:var(--navy);color:var(--green);font-family:"Open Sans",sans-serif;font-size:23px;font-weight:300;text-align:right;padding-right:14px;line-height:31px;z-index:2}
.contact-bar strong{color:#fff;font-weight:600}
.portrait{left:414px;top:427px;width:132px;height:103px;background:linear-gradient(180deg,#dcdcdc 0%,#ececec 100%)}
.contact-list{position:absolute;left:558px;top:436px;list-style:none;font-family:"Open Sans",sans-serif;font-size:16px;color:var(--ink-dark);line-height:21.5px}
.contact-list li{display:flex;align-items:center;gap:8px}
.contact-list svg{width:12px;height:12px;fill:var(--green)}
</style>
</head>
<body>

<section class="flyer flyer-back">
  <div class="photo back-hero" role="img" aria-label="Photo of a brick conservatory with white windows and a garden"></div>
  <div class="brick-field back-pattern" role="img" aria-label="Green brick pattern decoration"></div>
  <div class="about">
    <p>We have many years of experience in the building trade. From new builds and renovations to extensions and loft/garage conversions. No job to big or too small.</p>
    <p>We are one of the lucky few that actually enjoy our jobs. That's what serves us best in putting the extra care and attention into our customers' homes.</p>
    <p>We provide a value-added construction service to our customers by creating a successful partnership. Our pledge is to establish lasting relationships with our customers by exceeding their expectations through exceptional professionalism and quality of work by all of our construction team.</p>
    <p>We want stonvale to be more than just our company name to you. We give our customers a personal professional service and work on each project as if it was our own home.</p>
    <p>It would be an honor to bring your grand designs to life and meeting our team and seeing our work will definitely fill you with confidence.</p>
  </div>
  <div class="photo gallery-1" role="img" aria-label="Photo of a curved flower bed with a stone edge and lawn"></div>
  <div class="photo gallery-2" role="img" aria-label="Photo of a paved garden patio with table and parasol"></div>
  <div class="photo gallery-3" role="img" aria-label="Photo of a timber deck with garden chairs"></div>
</section>

<section class="flyer flyer-front">
  <div class="brick-field front-pattern" role="img" aria-label="Cascading green brick pattern decoration"></div>
  <div class="hero-frame">
    <div class="photo hero-photo" role="img" aria-label="Photo of a brick garden wall with a round window and planters"></div>
  </div>
  <div class="services">
    <div style="font-size:29px;margin-top:4px">Brick Walls</div>
    <div style="font-size:47px">Patios &amp; Decking</div>
    <div style="font-size:31px">Conservatories <span style="font-size:20px">Fencing</span></div>
    <div style="font-size:21px;margin-top:3px">Garage Convertions<span style="font-size:31px">Driveways</span></div>
    <div style="font-size:36px">Extensions <span style="font-size:22px">Garage Convertions</span></div>
    <div style="font-size:24px;margin-top:2px">Fascias &amp; Soffits</div>
    <div style="font-size:30px;margin-top:2px">Propery Alterations <span style="font-size:22px">Guttering</span></div>
  </div>
  <div class="footer-band"></div>
  <div class="footer-rule"></div>
  <div class="brand">
    <div class="brand-name"><span class="brand-mark"></span>stonvale</div>
    <div class="brand-tag">Building Services</div>
  </div>
  <div class="photo portrait" role="img" aria-label="Portrait photo of the builder in a white shirt"></div>
  <div class="contact-bar">Contact <strong>DECLAN</strong></div>
  <ul class="contact-list">
    <li><svg viewBox="0 0 12 12"><path d="M2.5 0.5l2 2.2-1.1 1.4c.7 1.6 2 2.9 3.5 3.6l1.4-1.1 2.2 2-1.3 2.1C4.8 10.4 1.5 7.1 0.3 1.9z"/></svg>01632 960418</li>
    <li><svg viewBox="0 0 12 12"><rect x="3" y="0.5" width="6" height="11" rx="1"/><rect x="4" y="2" width="4" height="6" fill="#fff"/></svg>07700 900627</li>
    <li><svg viewBox="0 0 12 12"><rect x="0.5" y="2.5" width="11" height="7"/><path d="M0.5 2.5L6 7l5.5-4.5" stroke="#fff" fill="none"/></svg>info@stonvale.co.uk</li>
    <li><svg viewBox="0 0 12 12"><circle cx="6" cy="6" r="5.5"/><path d="M0.5 6h11M6 .5v11M2.5 2.5c2 1.3 5 1.3 7 0M2.5 9.5c2-1.3 5-1.3 7 0" stroke="#fff" stroke-width=".7" fill="none"/></svg>www.stonvale.co.uk</li>
  </ul>
</section>

</body>
</html>
```